HearthBay business card and stationary design

We are looking for a simple yet elegant design for our mortgage company business card and stationary.

The card should include:
Name (Doug Warley)
Title (CEO)
Phone Number (614-382-9047)
Address (48 Birchwood Terrace, Suite 315, Marlow, NJ 08214)
Email (email@hearthbay.example)
"NMLS" i.e. (NMLS 61947)
"Company NMLS" (Company NMLS 492716)

Contact Information for Business Card

See above

```html
<!DOCTYPE html>
<html lang="en">
<head>
<meta charset="utf-8">
<title>HearthBay Business Card</title>
<link rel="stylesheet" href="https://fonts.googleapis.com/css2?family=Montserrat:wght@400;500;600;700&display=swap">
<style>
  :root {
    --backdrop: #141619;
    --card: #1c2631;
    --card-deep: #18202a;
    --accent: #2aa3e6;
    --ink: #ffffff;
    --ink-soft: #e6edf3;
  }
  html, body {
    margin: 0;
    padding: 0;
    width: 1200px;
    height: 864px;
    overflow: hidden;
    background: var(--backdrop);
    font-family: "Montserrat", Arial, sans-serif;
  }
  .canvas {
    position: relative;
    width: 1200px;
    height: 864px;
  }
  .card {
    position: absolute;
    left: 330px;
    width: 540px;
    height: 309px;
    background: linear-gradient(135deg, var(--card) 0%, var(--card-deep) 100%);
    box-shadow: 0 14px 36px rgba(0,0,0,0.55);
    overflow: hidden;
  }
  .card--front { top: 58px; }
  .card--back { top: 410px; }

  .wordmark {
    position: absolute;
    font-weight: 600;
    color: var(--ink);
    letter-spacing: 0.5px;
    white-space: nowrap;
  }
  .card--front .wordmark {
    left: 0; right: 0; top: 118px;
    text-align: center;
    font-size: 60px;
    line-height: 72px;
  }
  .card--back .wordmark {
    left: 250px; top: 42px;
    font-size: 38px;
    line-height: 46px;
  }

  .licence {
    position: absolute;
    left: 34px; top: 112px;
    font-size: 12.5px;
    line-height: 20px;
    color: var(--ink-soft);
  }
  .person {
    position: absolute;
    left: 0; top: 166px;
    display: flex;
    align-items: stretch;
  }
  .person__bar {
    width: 12px;
    background: var(--accent);
    margin-right: 20px;
  }
  .person__name {
    font-size: 19px;
    font-weight: 700;
    color: var(--accent);
    line-height: 22px;
    letter-spacing: 0.3px;
  }
  .person__title {
    font-size: 14px;
    font-weight: 700;
    color: var(--ink);
    line-height: 18px;
  }
  .divider {
    position: absolute;
    left: 32px; right: 22px; top: 218px;
    height: 1.5px;
    background: var(--accent);
  }
  .address {
    position: absolute;
    right: 26px; top: 168px;
    text-align: right;
    font-size: 12.5px;
    line-height: 19px;
    color: var(--ink-soft);
  }
  .contacts {
    position: absolute;
    left: 34px; top: 230px;
    margin: 0; padding: 0;
    list-style: none;
  }
  .contacts li {
    display: flex;
    align-items: center;
    gap: 12px;
    font-size: 13px;
    line-height: 23px;
    color: var(--ink-soft);
  }
  .contacts svg {
    width: 13px; height: 13px;
    fill: var(--accent);
    flex: none;
  }
</style>
</head>
<body>
<main class="canvas">
  <section class="card card--front" aria-label="Card front">
    <div class="wordmark">HearthBay</div>
  </section>

  <section class="card card--back" aria-label="Card back">
    <div class="wordmark">HearthBay</div>

    <div class="licence">
      "NMLS" i.e. (NMLS 61947)<br>
      Company NMLS 492716
    </div>

    <div class="person">
      <span class="person__bar"></span>
      <div>
        <div class="person__name">DOUG WARLEY</div>
        <div class="person__title">CEO</div>
      </div>
    </div>

    <div class="address">
      48 Birchwood Terrace, Suite<br>
      315, Marlow, NJ 08214)
    </div>

    <div class="divider"></div>

    <ul class="contacts">
      <li>
        <svg viewBox="0 0 16 16" aria-hidden="true"><path d="M3.6 1.2l2.3 2.6-1.3 1.8c.9 2 2.5 3.6 4.4 4.5l1.8-1.3 2.6 2.3-1.4 2.6C6.5 13.2 2.8 9.5 1 4z"/></svg>
        614-382-9047
      </li>
      <li>
        <svg viewBox="0 0 16 16" aria-hidden="true"><path d="M1 3h14v10H1z M2.5 4.5L8 8.6l5.5-4.1" fill="none" stroke="#2aa3e6" stroke-width="1.6"/></svg>
        email@hearthbay.example
      </li>
      <li>
        <svg viewBox="0 0 16 16" aria-hidden="true"><circle cx="8" cy="8" r="6.5" fill="none" stroke="#2aa3e6" stroke-width="1.5"/><path d="M1.5 8h13M8 1.5c-2.5 3-2.5 10 0 13M8 1.5c2.5 3 2.5 10 0 13" fill="none" stroke="#2aa3e6" stroke-width="1.2"/></svg>
        www.hearthbay.example
      </li>
    </ul>
  </section>
</main>
</body>
</html>
```